Create a Branded Four Stage Lifecycle Diagram

We need a rethink / redesign of our Lifecycle. We created it and have used it till now but it is not professional and needs our branding as well. We use it for presentations, for analysis with schools when we are consulting on site and it should look equally good on a powerpoint slide as on a handout and, of course, as a JPG that we can copy onto documents that we create. It does not have to look like what we currently have. I will include the article so you can see what we are trying to achieve. Eventually we want to be able to trademark it. It should include copyright 2020 Harbor Academy Advisors. Each stafe should reflect its characteristics in some fashion.

Target Market(s)

We serve K-12 Christian private schools

Industry/Entity Type

Education

Font styles to use
Sans Serif

Colors

Designer to choose colors to be used in the design.

Requirements
Must have
• HAA logo
• copyright notice
• title: HAA Lifecycle
Nice to have
• In the article, you will see the Corporate Lifecycle. It is completely different from ours. You will also see our current 'design'. It does not have to be like the one we currently have - it is not a refresh - it is a new design.
Should not have
• There must be no chance that our design could be confused with the corporate lifecycle.

```html
<!DOCTYPE html>
<html lang="en">
<head>
<meta charset="utf-8">
<title>The HAA Christian School Lifecycle</title>
<link rel="stylesheet" href="https://fonts.googleapis.com/css2?family=Arvo:wght@400;700&family=Open+Sans:wght@400;700&family=Arimo&display=swap">
<style>
  :root {
    --bg: #ffffff;
    --ring: #e3e7e8;
    --shadow: #c7cfcd;
    --dot: #3d3d3d;
    --entre-dark: #4a55a5;
    --entre-light: #5b67c8;
    --entre-label: #4f57a8;
    --entre-knob: #a6dfe5;
    --adol-dark: #4e7fb0;
    --adol-light: #6a9fd8;
    --adol-label: #4f7fb0;
    --adol-knob: #8fc3e6;
    --mature-dark: #3f8fcf;
    --mature-light: #72b0e0;
    --mature-label: #3f8fcf;
    --mature-knob: #6f9bd6;
    --dying-dark: #5a9e9e;
    --dying-light: #7cc4c6;
    --dying-label: #3a8c8c;
    --dying-knob: #5b5fc7;
    --brand: #4f57a8;
    --tagline: #8a8f93;
    --ink: #111111;
  }
  html, body {
    margin: 0;
    padding: 0;
    width: 1200px;
    height: 1200px;
    overflow: hidden;
    background: var(--bg);
  }
  .canvas {
    position: relative;
    width: 1200px;
    height: 1200px;
  }
  .diagram {
    position: absolute;
    left: 0;
    top: 0;
    width: 1200px;
    height: 1200px;
  }
  .stage-label {
    font-family: "Arvo", serif;
    font-weight: 700;
    font-size: 46px;
  }
  .stage-years {
    font-family: "Arvo", serif;
    font-weight: 700;
    fill: #ffffff;
    stroke-width: 2.5px;
    paint-order: stroke;
    text-anchor: middle;
  }
  .path-dotted {
    fill: none;
    stroke: var(--shadow);
    stroke-width: 9;
    stroke-dasharray: 11 9;
  }
  .path-solid {
    fill: none;
    stroke: var(--shadow);
    stroke-width: 9;
    stroke-linecap: round;
  }
  .path-arrow {
    fill: none;
    stroke: var(--shadow);
    stroke-width: 9;
    stroke-linejoin: round;
  }
  .knob-bar { stroke: var(--shadow); stroke-width: 10; }
  .end-dot { fill: var(--dot); }
  .brand-name {
    font-family: "Open Sans", sans-serif;
    font-weight: 700;
    font-size: 84px;
    fill: var(--brand);
    text-anchor: middle;
    letter-spacing: 4px;
  }
  .brand-tagline {
    font-family: "Open Sans", sans-serif;
    font-weight: 400;
    font-size: 16px;
    fill: var(--tagline);
    text-anchor: middle;
  }
  .title {
    position: absolute;
    left: 0;
    width: 1200px;
    top: 1034px;
    margin: 0;
    text-align: center;
    font-family: "Open Sans", sans-serif;
    font-weight: 400;
    font-size: 50px;
    color: var(--ink);
    line-height: 1;
  }
  .title strong { font-weight: 700; }
  .copyright {
    position: absolute;
    left: 0;
    width: 1200px;
    top: 1135px;
    margin: 0;
    text-align: center;
    font-family: "Arimo", sans-serif;
    font-size: 22px;
    line-height: 1;
    color: var(--ink);
  }
</style>
</head>
<body>
<main class="canvas">
  <svg class="diagram" viewBox="0 0 1500 1500" width="1200" height="1200" aria-label="Four stage lifecycle diagram">
    <defs>
      <clipPath id="inner-disc"><circle cx="0" cy="0" r="102"/></clipPath>
    </defs>

    <g class="brand">
      <text class="brand-name" x="1240" y="238">HAA</text>
      <text class="brand-tagline" x="1240" y="271">guidance · growth · stewardship</text>
    </g>

    <g class="connectors">
      <path class="path-dotted" d="M645 95 A175 175 0 0 0 475 300 A175 175 0 0 0 600 440 C680 455 722 470 730 525"/>
      <path class="path-arrow" d="M732 535 L736 565 L752 565 M744 556 L754 565 L744 574"/>
      <circle class="end-dot" cx="645" cy="95" r="8"/>
      <circle class="end-dot" cx="730" cy="525" r="8"/>

      <path class="path-dotted" d="M928 354 A175 175 0 0 1 1105 532 A175 175 0 0 1 960 700 C880 712 852 740 849 783"/>
      <path class="path-arrow" d="M849 793 L846 815 L830 818 M838 808 L828 818 L836 828"/>
      <circle class="end-dot" cx="928" cy="354" r="8"/>
      <circle class="end-dot" cx="849" cy="783" r="8"/>

      <path class="path-dotted" d="M642 619 A175 175 0 0 0 472 820 A175 175 0 0 0 600 960 C676 975 718 990 727 1050"/>
      <path class="path-arrow" d="M729 1060 L733 1090 L749 1090 M741 1081 L751 1090 L741 1099"/>
      <circle class="end-dot" cx="642" cy="619" r="8"/>
      <circle class="end-dot" cx="727" cy="1050" r="8"/>

      <path class="path-solid" d="M905 873 A177 177 0 0 1 905 1228"/>
      <circle class="end-dot" cx="905" cy="873" r="8"/>
      <circle class="end-dot" cx="905" cy="1228" r="8"/>
    </g>

    <g class="stage stage-entrepreneur" transform="translate(630 268)">
      <circle cx="45" cy="33" r="127" fill="var(--shadow)"/>
      <circle r="125" fill="var(--ring)"/>
      <circle r="102" fill="var(--entre-dark)"/>
      <circle cx="20" cy="20" r="100" fill="var(--entre-light)" clip-path="url(#inner-disc)"/>
      <text class="stage-years" y="-17" font-size="46" stroke="var(--entre-dark)">0-10</text>
      <text class="stage-years" y="45" font-size="44" stroke="var(--entre-dark)">Years</text>
    </g>
    <line class="knob-bar" x1="403" y1="272" x2="467" y2="272"/>
    <circle class="end-dot" cx="403" cy="272" r="8"/>
    <circle cx="467" cy="272" r="14" fill="#ffffff" stroke="var(--entre-knob)" stroke-width="8"/>
    <text class="stage-label" x="378" y="287" text-anchor="end" fill="var(--entre-label)">Entrepreneur</text>

    <g class="stage stage-adolescent" transform="translate(915 518)">
      <circle cx="45" cy="33" r="127" fill="var(--shadow)"/>
      <circle r="125" fill="var(--ring)"/>
      <circle r="102" fill="var(--adol-dark)"/>
      <circle cx="20" cy="20" r="100" fill="var(--adol-light)" clip-path="url(#inner-disc)"/>
      <text class="stage-years" y="-11" font-size="46" stroke="var(--adol-dark)">10-15</text>
      <text class="stage-years" y="51" font-size="44" stroke="var(--adol-dark)">Years</text>
    </g>
    <line class="knob-bar" x1="1105" y1="532" x2="1170" y2="532"/>
    <circle class="end-dot" cx="1170" cy="532" r="8"/>
    <circle cx="1105" cy="532" r="14" fill="#ffffff" stroke="var(--adol-knob)" stroke-width="8"/>
    <text class="stage-label" x="1203" y="547" fill="var(--adol-label)">Adolescent</text>

    <g class="stage stage-mature" transform="translate(630 778)">
      <circle cx="45" cy="33" r="127" fill="var(--shadow)"/>
      <circle r="125" fill="var(--ring)"/>
      <circle r="102" fill="var(--mature-dark)"/>
      <circle cx="20" cy="20" r="100" fill="var(--mature-light)" clip-path="url(#inner-disc)"/>
      <text class="stage-years" x="2" y="-7" font-size="46" stroke="var(--mature-dark)">15-30+</text>
      <text class="stage-years" x="4" y="53" font-size="44" stroke="var(--mature-dark)">Years</text>
    </g>
    <line class="knob-bar" x1="403" y1="791" x2="467" y2="791"/>
    <circle class="end-dot" cx="403" cy="791" r="8"/>
    <circle cx="467" cy="791" r="14" fill="#ffffff" stroke="var(--mature-knob)" stroke-width="8"/>
    <text class="stage-label" x="378" y="805" text-anchor="end" fill="var(--mature-label)">Mature</text>

    <g class="stage stage-dying" transform="translate(890 1037)">
      <circle cx="45" cy="33" r="127" fill="var(--shadow)"/>
      <circle r="125" fill="var(--ring)"/>
      <circle r="102" fill="var(--dying-dark)"/>
      <circle cx="20" cy="20" r="100" fill="var(--dying-light)" clip-path="url(#inner-disc)"/>
      <text class="stage-years" y="-12" font-size="46" stroke="var(--dying-dark)">20+</text>
      <text class="stage-years" y="50" font-size="44" stroke="var(--dying-dark)">Years</text>
    </g>
    <line class="knob-bar" x1="1082" y1="1050" x2="1147" y2="1050"/>
    <circle class="end-dot" cx="1147" cy="1050" r="8"/>
    <circle cx="1082" cy="1050" r="14" fill="#ffffff" stroke="var(--dying-knob)" stroke-width="8"/>
    <text class="stage-label" x="1167" y="1065" fill="var(--dying-label)">Dying</text>
  </svg>

  <h1 class="title">The HAA Christian School <strong>“Lifecycle”</strong></h1>
  <p class="copyright">© copyright 2020 Harbor Academy Advisors</p>
</main>
</body>
</html>
```